Powerpoint presentation sales pack for ground transfer company

Need a base pack for sales presentation for KVT,
We specialise in corporate ground transport (similar to ZOLTA)
Needs to be sharp and have a modern feel
Looking for a good master slide design and page layout for provide content
Check out our website https://kvt.example/
Check out our competitors https://www.zolta.example/business https://www.hollisterlimorun.example.au
Look at other marketing material available and old draft powerpoint pack for content and design ideas

```html
<!DOCTYPE html>
<html lang="en">
<head>
<meta charset="utf-8">
<title>KVT – Corporate Ground Transport Sales Pack</title>
<link href="https://fonts.googleapis.com/css2?family=Montserrat:wght@400;500;600;700&display=swap" rel="stylesheet">
<style>
:root{
  --teal:#127c71;
  --teal-dark:#0d5f56;
  --teal-soft:#5fb3a9;
  --ink:#111;
  --grey:#7a7a7a;
  --grey-mid:#8e8e8e;
  --grey-light:#e6e6e6;
  --text:#5e5e5e;
  --paper:#fff;
  --sheet:#d9d9d9;
  --glow:radial-gradient(ellipse at 32% 30%,rgba(255,255,255,.38),rgba(255,255,255,0) 55%);
  --shade:radial-gradient(ellipse at 78% 85%,rgba(0,0,0,.28),rgba(0,0,0,0) 60%);
}
*{box-sizing:border-box;margin:0;padding:0}
html,body{width:1200px;height:2712px;overflow:hidden;background:var(--sheet)}
body{font-family:"Montserrat",Arial,sans-serif;color:var(--ink)}
.deck{display:grid;grid-template-columns:repeat(3,389px);grid-template-rows:repeat(12,219px);gap:7px;padding:3px 9px;width:1200px;height:2712px}
.slide{position:relative;background:var(--paper);overflow:hidden}
.title{position:absolute;top:11px;left:12px;font-size:12.5px;font-weight:600;color:var(--teal-dark)}
.title::after{content:"";display:block;width:26px;height:2px;background:var(--teal);margin-top:3px}
.logo{position:absolute;top:9px;right:12px;font-size:13px;font-weight:700;color:var(--ink);letter-spacing:.5px}
.foot{position:absolute;left:0;right:0;bottom:0;height:9px;background:var(--teal);font-size:3.6px;color:#fff;padding:2.5px 12px}
.foot::after{content:"";position:absolute;right:0;top:0;width:22px;height:9px;background:var(--ink)}

/* photo areas: soft tonal gradients */
.ph{position:absolute;background:var(--glow),var(--shade),linear-gradient(160deg,#e6e1da 0%,#c2b8ab 45%,#857b70 100%)}
.ph.cabin{background:var(--glow),var(--shade),linear-gradient(140deg,#e9dccb 0%,#b79f86 40%,#5d5047 75%,#2f2a27 100%)}
.ph.terminal{background:var(--glow),var(--shade),linear-gradient(165deg,#eef2f4 0%,#c7d1d6 35%,#8d9aa1 70%,#56616a 100%)}
.ph.office{background:var(--glow),var(--shade),linear-gradient(150deg,#f3eee6 0%,#d6c9b6 45%,#9d8c78 100%)}
.ph.dark{background:radial-gradient(ellipse at 70% 35%,rgba(255,255,255,.18),rgba(255,255,255,0) 55%),linear-gradient(150deg,#55585b 0%,#34373a 50%,#16181a 100%)}
.ph.night{background:radial-gradient(ellipse at 50% 40%,rgba(210,190,150,.25),rgba(0,0,0,0) 60%),linear-gradient(180deg,#4a4c4f 0%,#2a2b2d 60%,#121314 100%)}
.ph.teal{background:radial-gradient(ellipse at 30% 30%,rgba(255,255,255,.22),rgba(255,255,255,0) 55%),linear-gradient(135deg,#4aa69c 0%,#1d8075 45%,#0c524a 100%)}
.ph.city{background:linear-gradient(180deg,#fafafa 0%,#ececec 40%,#d6d6d6 100%)}
.ph.map{background:radial-gradient(ellipse at 25% 40%,#d2d7d7,rgba(210,215,215,0) 35%),radial-gradient(ellipse at 60% 45%,#cdd3d3,rgba(205,211,211,0) 40%),radial-gradient(ellipse at 85% 65%,#d6dada,rgba(214,218,218,0) 30%),#eef0f0}
.ph.usmap{background:radial-gradient(ellipse at 50% 50%,#cfcfcf,rgba(207,207,207,0) 70%),#ececec}
.ph.face{background:radial-gradient(circle at 40% 35%,#e8ddd0,#b9a894 60%,#7f7263 100%)}
.ph.round{border-radius:50%}

.tx{font-size:4.6px;line-height:1.4;color:var(--text)}
.tx.w{color:#fff}
.h{font-size:6px;font-weight:600;color:var(--ink)}
.h.w{color:#fff}
.h.t{color:var(--teal)}
.abs{position:absolute}
.ico{position:absolute;width:13px;height:13px;border-radius:50%;background:var(--teal);display:flex;align-items:center;justify-content:center}
.ico svg{width:7px;height:7px;fill:none;stroke:#fff;stroke-width:2}
.ico.k{background:var(--ink)}
.ico.g{background:var(--grey)}
.ico.sq{border-radius:2px}
.ring{position:absolute;border-radius:50%;border:1px solid #fff;display:flex;align-items:center;justify-content:center}
.ring svg{width:40%;height:40%;fill:none;stroke:#fff;stroke-width:1.6}
.big{font-weight:700;color:var(--teal)}
table{border-collapse:collapse}
</style>
</head>
<body>
<svg width="0" height="0" style="position:absolute" aria-hidden="true">
  <symbol id="tick" viewBox="0 0 20 20"><path d="M4 10.5l4 4 8-9"/></symbol>
  <symbol id="arrow" viewBox="0 0 20 20"><path d="M4 10h12M11 5l5 5-5 5"/></symbol>
  <symbol id="pin" viewBox="0 0 20 20"><path d="M10 18s6-6 6-10a6 6 0 0 0-12 0c0 4 6 10 6 10z"/><circle cx="10" cy="8" r="2"/></symbol>
  <symbol id="phone" viewBox="0 0 20 20"><path d="M5 3h3l2 5-2 1a9 9 0 0 0 3 3l1-2 5 2v3a2 2 0 0 1-2 2A14 14 0 0 1 3 5a2 2 0 0 1 2-2z"/></symbol>
  <symbol id="gear" viewBox="0 0 20 20"><circle cx="10" cy="10" r="3"/><circle cx="10" cy="10" r="7"/></symbol>
  <symbol id="star" viewBox="0 0 20 20"><path d="M10 2l2.4 5.2 5.6.6-4.2 3.8 1.2 5.6L10 14.4 5 17.2l1.2-5.6L2 7.8l5.6-.6z"/></symbol>
  <symbol id="search" viewBox="0 0 20 20"><circle cx="8.5" cy="8.5" r="5"/><path d="M12.5 12.5l5 5"/></symbol>
  <symbol id="user" viewBox="0 0 20 20"><circle cx="10" cy="6.5" r="3.5"/><path d="M3 18a7 7 0 0 1 14 0"/></symbol>
</svg>

<main class="deck">

<!-- 1 Cover -->
<section class="slide">
  <div class="logo" style="left:12px;right:auto">KVT</div>
  <div class="ph terminal" style="left:0;right:0;top:40px;height:128px;background:radial-gradient(ellipse at 75% 30%,rgba(255,255,255,.2),rgba(255,255,255,0) 50%),linear-gradient(120deg,#58646b 0%,#3a444a 45%,#1d2328 100%)" role="img" aria-label="Business travellers in an airport terminal"></div>
  <div class="abs" style="top:84px;right:24px;text-align:right">
    <div style="font-size:15px;font-weight:500;color:#fff">YOUR TITLE GOES HERE</div>
    <div style="font-size:5px;color:#fff;margin-top:3px">Your Subtitle Goes Here</div>
  </div>
  <div class="abs tx" style="right:12px;bottom:8px;font-size:4px">kvt.example</div>
</section>

<!-- 2 Cover teal -->
<section class="slide">
  <div class="logo">KVT</div>
  <div class="ph teal" style="left:0;right:0;top:40px;height:128px" role="img" aria-label="Chauffeur opening a car door, teal tint"></div>
  <div class="abs" style="top:84px;left:28px">
    <div style="font-size:15px;font-weight:500;color:#fff">YOUR TITLE GOES HERE</div>
    <div style="font-size:5px;color:#fff;margin-top:3px">Your Subtitle Goes Here</div>
  </div>
</section>

<!-- 3 About Us -->
<section class="slide">
  <div class="title">About Us</div>
  <div class="logo">KVT</div>
  <div class="abs tx" style="left:12px;right:12px;top:38px">
    <p style="margin-bottom:6px">We move corporate guests between airports, hotels, offices and events with trained chauffeurs, late-model sedans and live tracking. Every booking is confirmed in minutes, every driver is vetted, and every trip is logged for your finance team. Our dispatch desk runs day and night so schedule changes never leave a passenger waiting at the kerb.</p>
    <p style="margin-bottom:6px">From single executive transfers to coach shuttles for large conferences, we plan the route, assign the right vehicle and keep your travel manager informed. Flight monitoring adjusts pickups automatically, meet and greet staff hold clear name boards, and consolidated monthly invoicing keeps accounts simple and transparent.</p>
    <p>Our fleet covers every major city and regional hub, with fixed corporate rates, priority support and a single account for all your teams. We measure ourselves on punctuality, comfort and safety, and we report on all three every month so you can see exactly how your people travel.</p>
  </div>
  <div class="foot">© Copyright 2025 KVT. All rights reserved.</div>
</section>

<!-- 4 Agenda -->
<section class="slide">
  <div class="title">Our Agenda</div>
  <div class="logo">KVT</div>
  <div class="ico sq" style="left:18px;top:44px"><svg><use href="#star"/></svg></div>
  <div class="abs" style="left:38px;top:43px"><div class="h" style="font-weight:500">Agenda One</div><div class="tx">Short note here</div></div>
  <div class="ico sq k" style="left:18px;top:76px"><svg><use href="#pin"/></svg></div>
  <div class="abs" style="left:38px;top:75px"><div class="h" style="font-weight:500">Agenda Two</div><div class="tx">Short note here</div></div>
  <div class="ico sq g" style="left:18px;top:108px"><svg><use href="#gear"/></svg></div>
  <div class="abs" style="left:38px;top:107px"><div class="h" style="font-weight:500">Agenda Three</div><div class="tx">Short note here</div></div>
  <div class="ico sq" style="left:200px;top:44px"><svg><use href="#user"/></svg></div>
  <div class="abs" style="left:220px;top:43px"><div class="h" style="font-weight:500">Agenda Four</div><div class="tx">Short note here</div></div>
  <div class="ico sq k" style="left:200px;top:76px"><svg><use href="#phone"/></svg></div>
  <div class="abs" style="left:220px;top:75px"><div class="h" style="font-weight:500">Agenda Five</div><div class="tx">Short note here</div></div>
  <div class="ico sq g" style="left:200px;top:108px"><svg><use href="#search"/></svg></div>
  <div class="abs" style="left:220px;top:107px"><div class="h" style="font-weight:500">Agenda Six</div><div class="tx">Short note here</div></div>
  <div class="foot">© Copyright 2025 KVT. All rights reserved.</div>
</section>

<!-- 5 Market Overview -->
<section class="slide">
  <div class="title">Market Overview</div>
  <div class="logo">KVT</div>
  <div class="abs" style="left:12px;top:40px;width:62px;height:64px;background:var(--grey-mid);padding:5px 4px"><div class="h w" style="font-size:4.6px">Heading Text</div><div class="tx w">Brief market note goes here.</div></div>
  <div class="ph cabin" style="left:74px;top:34px;width:86px;height:70px" role="img" aria-label="Smiling passenger in a car"></div>
  <div class="abs" style="left:160px;top:40px;width:80px;height:64px;background:var(--teal)"></div>
  <div class="ring" style="left:178px;top:50px;width:44px;height:44px;border:3px solid #fff"><span style="font-size:10px;font-weight:600;color:#fff">60%</span></div>
  <div class="abs" style="left:240px;top:40px;width:40px;height:64px;background:var(--teal-dark)"></div>
  <div class="abs" style="left:285px;top:40px;width:90px"><div class="h" style="font-size:4.6px">Heading Text</div><div class="tx">Brief market note goes here for this point.</div><div class="h" style="font-size:4.6px;margin-top:6px">Heading Text</div><div class="tx">Brief market note goes here for this point.</div></div>
  <div class="abs" style="left:12px;top:110px;width:60px"><div class="h" style="font-size:4.6px">Heading Text</div><div class="tx">Brief note here.</div></div>
  <div class="abs" style="left:80px;top:110px;width:295px"><div class="h" style="font-size:5px">Heading Text</div><div class="tx">Corporate transfer demand keeps rising as firms return to travel. Buyers want one trusted partner, clear fixed pricing, real-time updates and detailed reporting across every city their teams visit.</div></div>
  <div class="foot">© Copyright 2025 KVT. All rights reserved.</div>
</section>

<!-- 6 Bullets -->
<section class="slide">
  <div class="title">Bullets Point 1 Level</div>
  <div class="logo">KVT</div>
  <div class="abs" style="left:16px;top:44px;width:100px"><div class="h">● Your Text Here</div><div class="tx">Add a short supporting line about this point.</div></div>
  <div class="abs" style="left:140px;top:44px;width:100px"><div class="h">● Your Text Here</div><div class="tx">Add a short supporting line about this point.</div></div>
  <div class="abs" style="left:264px;top:44px;width:100px"><div class="h" style="color:var(--grey)">● Your Text Here</div><div class="tx">Add a short supporting line about this point.</div></div>
  <div class="abs" style="left:16px;top:84px;width:100px"><div class="h">● Your Text Here</div><div class="tx">Add a short supporting line about this point.</div></div>
  <div class="abs" style="left:140px;top:84px;width:100px"><div class="h">● Your Text Here</div><div class="tx">Add a short supporting line about this point.</div></div>
  <div class="abs" style="left:264px;top:84px;width:100px"><div class="h" style="color:var(--grey)">● Your Text Here</div><div class="tx">Add a short supporting line about this point.</div></div>
  <div class="abs tx" style="left:16px;right:16px;top:128px">Use this area to expand on the bullets above with a short paragraph that ties the points together and leads into the next slide of the pack.</div>
  <div class="foot">© Copyright 2025 KVT. All rights reserved.</div>
</section>

<!-- 7 Photo collage -->
<section class="slide">
  <div class="ph cabin" style="left:0;top:0;width:195px;height:219px" role="img" aria-label="Couple smiling in the back of a car"></div>
  <div class="ph office" style="left:195px;top:0;width:194px;height:110px" role="img" aria-label="Passenger looking back from the front seat"></div>
  <div class="ph cabin" style="left:195px;top:110px;width:194px;height:109px" role="img" aria-label="Passenger and chauffeur in a car"></div>
  <div class="abs" style="left:0;top:0;width:160px;height:56px;background:var(--ink);padding:6px 8px"><div class="tx w">Ride in comfort with a vetted chauffeur, clean late-model sedan and a fixed corporate rate on every trip.</div></div>
  <div class="abs" style="left:160px;top:76px;width:140px;height:56px;background:var(--ink);padding:6px 8px"><div class="tx w">Flight tracking adjusts your pickup time so your driver is always waiting at arrivals.</div></div>
  <div class="abs" style="left:0;top:148px;width:150px;height:62px;background:var(--teal);padding:6px 8px"><div class="tx w">One account, one invoice and live reporting for every traveller in your company.</div></div>
  <div class="foot">© Copyright 2025 KVT. All rights reserved.</div>
</section>

<!-- 8 Four columns -->
<section class="slide">
  <div class="title">Your Title Here</div>
  <div class="logo">KVT</div>
  <div class="abs" style="left:12px;top:42px;width:90px;height:150px;background:var(--teal);padding:8px 7px;text-align:center"><div class="ring" style="position:static;margin:0 auto 4px;width:16px;height:16px"><svg><use href="#star"/></svg></div><div class="h w">Heading Here</div><div class="tx w" style="text-align:left;margin-top:3px">Explain one service pillar here in a few short lines of copy.</div></div>
  <div class="abs" style="left:103px;top:42px;width:90px;height:150px;background:var(--ink);padding:8px 7px;text-align:center"><div class="ring" style="position:static;margin:0 auto 4px;width:16px;height:16px"><svg><use href="#user"/></svg></div><div class="h w">Heading Here</div><div class="tx w" style="text-align:left;margin-top:3px">Explain one service pillar here in a few short lines of copy.</div></div>
  <div class="abs" style="left:194px;top:42px;width:90px;height:150px;background:var(--grey);padding:8px 7px;text-align:center"><div class="ring" style="position:static;margin:0 auto 4px;width:16px;height:16px"><svg><use href="#gear"/></svg></div><div class="h w">Heading Here</div><div class="tx w" style="text-align:left;margin-top:3px">Explain one service pillar here in a few short lines of copy.</div></div>
  <div class="abs" style="left:285px;top:42px;width:92px;height:150px;background:var(--teal);padding:8px 7px;text-align:center"><div class="ring" style="position:static;margin:0 auto 4px;width:16px;height:16px"><svg><use href="#search"/></svg></div><div class="h w">Heading Here</div><div class="tx w" style="text-align:left;margin-top:3px">Explain one service pillar here in a few short lines of copy.</div></div>
  <div class="foot">© Copyright 2025 KVT. All rights reserved.</div>
</section>

<!-- 9 Differences -->
<section class="slide">
  <div class="title">Our Differences</div>
  <div class="logo">KVT</div>
  <div class="abs" style="left:12px;top:44px;width:215px;height:120px;background:var(--teal)"></div>
  <div class="ico" style="left:20px;top:54px;background:#fff"><svg style="stroke:var(--teal)"><use href="#tick"/></svg></div><div class="abs tx w" style="left:40px;top:57px;width:170px">Fixed corporate rates with no surge pricing.</div>
  <div class="ico" style="left:20px;top:80px;background:#fff"><svg style="stroke:var(--teal)"><use href="#tick"/></svg></div><div class="abs tx w" style="left:40px;top:83px;width:170px">Vetted, uniformed chauffeurs on every trip.</div>
  <div class="ico" style="left:20px;top:106px;background:#fff"><svg style="stroke:var(--teal)"><use href="#tick"/></svg></div><div class="abs tx w" style="left:40px;top:109px;width:170px">Live flight tracking and 24/7 dispatch.</div>
  <div class="ico" style="left:20px;top:132px;background:#fff"><svg style="stroke:var(--teal)"><use href="#tick"/></svg></div><div class="abs tx w" style="left:40px;top:135px;width:170px">Monthly reporting and one simple invoice.</div>
  <div class="ph terminal" style="left:227px;top:44px;width:150px;height:120px" role="img" aria-label="Travellers with luggage in an airport hall"></div>
  <div class="foot">© Copyright 2025 KVT. All rights reserved.</div>
</section>

<!-- 10 Text & Bullet -->
<section class="slide">
  <div class="title">Text &amp; Bullet Area</div>
  <div class="logo">KVT</div>
  <div class="abs" style="left:12px;top:46px;width:115px"><div class="h">Heading Goes Here</div><div class="tx" style="margin-top:4px">Describe your corporate offer here in a short paragraph. Keep it to a few lines so the slide stays clean and easy to present.</div><div class="tx" style="margin-top:6px">Add a second note with a supporting detail or key figure for the client.</div></div>
  <div class="ico" style="left:148px;top:48px"><svg><use href="#tick"/></svg></div><div class="abs h t" style="left:166px;top:51px">Your Text Here</div>
  <div class="ico k" style="left:148px;top:78px"><svg><use href="#phone"/></svg></div><div class="abs h" style="left:166px;top:81px">Your Text Here</div>
  <div class="ico g" style="left:148px;top:108px"><svg><use href="#pin"/></svg></div><div class="abs h" style="left:166px;top:111px">Your Text Here</div>
  <div class="ico" style="left:148px;top:138px"><svg><use href="#star"/></svg></div><div class="abs h t" style="left:166px;top:141px">Your Text Here</div>
  <div class="ico" style="left:262px;top:48px"><svg><use href="#gear"/></svg></div><div class="abs h t" style="left:280px;top:51px">Your Text Here</div>
  <div class="ico k" style="left:262px;top:78px"><svg><use href="#user"/></svg></div><div class="abs h" style="left:280px;top:81px">Your Text Here</div>
  <div class="ico k" style="left:262px;top:108px"><svg><use href="#arrow"/></svg></div><div class="abs h" style="left:280px;top:111px">Your Text Here</div>
  <div class="ico" style="left:262px;top:138px"><svg><use href="#search"/></svg></div><div class="abs h t" style="left:280px;top:141px">Your Text Here</div>
  <div class="foot">© Copyright 2025 KVT. All rights reserved.</div>
</section>

<!-- 11 Clients -->
<section class="slide">
  <div class="abs" style="left:24px;top:18px;width:60px;height:22px;background:var(--grey-light)"></div>
  <div class="abs" style="left:116px;top:14px;width:56px;height:26px;background:var(--grey-light);border-radius:13px"></div>
  <div class="abs" style="left:204px;top:16px;width:70px;height:24px;background:var(--grey-light)"></div>
  <div class="abs" style="left:300px;top:18px;width:60px;height:22px;background:var(--grey-light)"></div>
  <div class="abs" style="left:24px;top:80px;width:54px;height:22px;background:var(--grey-light)"></div>
  <div class="abs" style="left:306px;top:84px;width:58px;height:16px;background:var(--grey-light);border-radius:8px"></div>
  <div class="abs" style="left:24px;top:160px;width:30px;height:30px;background:var(--grey-light);border-radius:50%"></div>
  <div class="abs" style="left:100px;top:158px;width:36px;height:36px;background:var(--grey-light);border-radius:50%"></div>
  <div class="abs" style="left:198px;top:160px;width:64px;height:28px;background:var(--grey-light)"></div>
  <div class="abs" style="left:298px;top:158px;width:52px;height:34px;background:var(--grey-light)"></div>
  <div class="abs" style="left:114px;top:62px;width:160px;height:64px;background:var(--teal);display:flex;align-items:center;justify-content:center;text-align:center"><div style="font-size:13px;font-weight:500;color:#fff;line-height:1.3">Our Awesome<br>Client</div></div>
</section>

<!-- 12 Dark five columns -->
<section class="slide" style="background:#2b2b2b">
  <div class="ph night" style="inset:0" role="img" aria-label="Dark city street at night"></div>
  <div class="abs" style="left:94px;top:28px;width:62px;height:56px;background:var(--teal)"></div>
  <div class="abs" style="left:218px;top:28px;width:62px;height:56px;background:var(--teal)"></div>
  <div class="ring" style="left:24px;top:46px;width:16px;height:16px;border:none"><svg style="width:100%;height:100%"><use href="#gear"/></svg></div>
  <div class="ring" style="left:117px;top:46px;width:16px;height:16px;border:none"><svg style="width:100%;height:100%"><use href="#user"/></svg></div>
  <div class="ring" style="left:180px;top:46px;width:16px;height:16px;border:none"><svg style="width:100%;height:100%"><use href="#search"/></svg></div>
  <div class="ring" style="left:241px;top:46px;width:16px;height:16px;border:none"><svg style="width:100%;height:100%"><use href="#star"/></svg></div>
  <div class="ring" style="left:346px;top:46px;width:16px;height:16px;border:none"><svg style="width:100%;height:100%"><use href="#gear"/></svg></div>
  <div class="abs" style="left:8px;top:96px;width:66px"><div class="h w">Heading Here</div><div class="tx w">Short point about the service here.</div></div>
  <div class="abs" style="left:82px;top:96px;width:66px"><div class="h w">Heading Here</div><div class="tx w">Short point about the service here.</div></div>
  <div class="abs" style="left:158px;top:96px;width:66px"><div class="h w">Heading Here</div><div class="tx w">Short point about the service here.</div></div>
  <div class="abs" style="left:234px;top:96px;width:66px"><div class="h w">Heading Here</div><div class="tx w">Short point about the service here.</div></div>
  <div class="abs" style="left:312px;top:96px;width:68px"><div class="h w">Heading Here</div><div class="tx w">Short point about the service here.</div></div>
</section>

<!-- 13 Mockup laptop -->
<section class="slide">
  <div class="title">Our Mockup Area</div>
  <div class="logo">KVT</div>
  <div class="abs" style="left:12px;top:150px;width:365px;height:50px;background:var(--grey-light)"></div>
  <div class="abs" style="left:90px;top:150px;width:200px;height:50px;background:var(--grey-mid)"></div>
  <div class="abs" style="left:106px;top:38px;width:178px;height:116px;background:#1b1b1b;border-radius:5px"></div>
  <div class="ph office" style="left:111px;top:43px;width:168px;height:104px" role="img" aria-label="Laptop screen showing a woman working"></div>
  <div class="abs" style="left:12px;top:60px;width:48px;height:12px;background:var(--ink);padding:3px 4px"><div class="tx w" style="font-size:3.6px;line-height:1.6">Your Text Here</div></div>
  <div class="abs" style="left:12px;top:96px;width:48px;height:12px;background:var(--ink);padding:3px 4px"><div class="tx w" style="font-size:3.6px;line-height:1.6">Your Text Here</div></div>
  <div class="abs" style="left:12px;top:132px;width:48px;height:12px;background:var(--teal);padding:3px 4px"><div class="tx w" style="font-size:3.6px;line-height:1.6">Your Text Here</div></div>
  <div class="abs" style="left:326px;top:60px;width:48px;height:12px;background:var(--teal);padding:3px 4px"><div class="tx w" style="font-size:3.6px;line-height:1.6">Your Text Here</div></div>
  <div class="abs" style="left:326px;top:96px;width:48px;height:12px;background:var(--ink);padding:3px 4px"><div class="tx w" style="font-size:3.6px;line-height:1.6">Your Text Here</div></div>
  <svg class="abs" style="left:0;top:0" width="389" height="219" aria-hidden="true"><g stroke="#999" stroke-width=".5"><line x1="60" y1="66" x2="130" y2="66"/><line x1="60" y1="102" x2="130" y2="102"/><line x1="60" y1="138" x2="130" y2="138"/><line x1="326" y1="66" x2="260" y2="66"/><line x1="326" y1="102" x2="260" y2="102"/></g></svg>
  <div class="foot">© Copyright 2025 KVT. All rights reserved.</div>
</section>

<!-- 14 Right picture -->
<section class="slide">
  <div class="ph teal" style="left:0;top:0;width:172px;height:219px" role="img" aria-label="Business traveller, teal tint"></div>
  <div class="ring" style="left:42px;top:36px;width:60px;height:60px;border:1.5px solid #fff"><span style="font-size:6.5px;font-weight:700;color:#fff;text-align:center;line-height:1.3">RIGHT<br>PICTURE<br>SLIDE</span></div>
  <div class="abs tx w" style="left:24px;top:148px;width:130px">Show your fleet and service here with one strong image and a short statement beside it.</div>
  <div class="logo">KVT</div>
  <svg class="abs" style="left:196px;top:38px" width="170" height="90" aria-label="Bar chart"><line x1="0" y1="80" x2="170" y2="80" stroke="#ccc" stroke-width=".6"/><g><rect x="8" y="40" width="8" height="40" fill="var(--ink)"/><rect x="18" y="20" width="8" height="60" fill="var(--teal)"/><rect x="48" y="50" width="8" height="30" fill="var(--ink)"/><rect x="58" y="10" width="8" height="70" fill="var(--teal)"/><rect x="88" y="30" width="8" height="50" fill="var(--ink)"/><rect x="98" y="45" width="8" height="35" fill="var(--grey)"/><rect x="128" y="15" width="8" height="65" fill="var(--ink)"/><rect x="138" y="35" width="8" height="45" fill="var(--teal)"/></g></svg>
  <div class="abs" style="left:196px;top:138px;font-size:16px;font-weight:600;color:var(--ink)"><span style="color:var(--teal);font-size:10px">▲</span> 85%</div>
  <div class="abs tx" style="left:214px;top:162px;width:150px">Growth in repeat corporate bookings year on year.</div>
  <div class="foot" style="left:172px">© Copyright 2025 KVT.</div>
</section>

<!-- 15 Mockup monitor -->
<section class="slide">
  <div class="abs" style="left:0;top:0;right:0;height:58px;background:var(--teal)"></div>
  <div class="title" style="color:#fff">Our Mockup Area</div>
  <div class="abs h" style="left:12px;top:66px">Heading Here</div>
  <div class="abs" style="left:206px;top:14px;width:168px;height:118px;background:#1f1f1f;border-radius:3px"></div>
  <div class="ph terminal" style="left:210px;top:18px;width:160px;height:106px" role="img" aria-label="Monitor showing family with luggage at airport"></div>
  <div class="abs" style="left:274px;top:132px;width:32px;height:12px;background:#bbb"></div>
  <div class="abs" style="left:262px;top:144px;width:56px;height:3px;background:#aaa"></div>
  <div class="ico" style="left:12px;top:94px"><svg><use href="#tick"/></svg></div><div class="abs tx" style="left:30px;top:95px;width:160px">Book online, by app or through your travel manager in seconds.</div>
  <div class="ico k" style="left:12px;top:120px"><svg><use href="#tick"/></svg></div><div class="abs tx" style="left:30px;top:121px;width:160px">Track every vehicle live from the moment it is dispatched.</div>
  <div class="ico" style="left:12px;top:146px"><svg><use href="#tick"/></svg></div><div class="abs tx" style="left:30px;top:147px;width:160px">Receive one clear invoice each month for all bookings.</div>
  <div class="foot">© Copyright 2025 KVT. All rights reserved.</div>
</section>

<!-- 16 Four photos -->
<section class="slide">
  <div class="title">Your Title Goes Here</div>
  <div class="logo">KVT</div>
  <div class="ph cabin" style="left:12px;top:42px;width:60px;height:48px" role="img" aria-label="Driver at the wheel"></div>
  <div class="abs" style="left:74px;top:42px;width:70px;height:48px;background:var(--ink);display:flex;align-items:center;justify-content:center"><span class="h w">Heading Goes Here</span></div>
  <div class="ph office" style="left:146px;top:42px;width:60px;height:48px" role="img" aria-label="Passengers in a car"></div>
  <div class="abs" style="left:12px;top:92px;width:60px;height:42px;background:var(--teal);display:flex;align-items:center;justify-content:center"><span class="h w">Heading Here</span></div>
  <div class="ph cabin" style="left:74px;top:92px;width:70px;height:42px" role="img" aria-label="Passenger smiling in the back seat"></div>
  <div class="abs" style="left:146px;top:92px;width:60px;height:42px;background:var(--grey);display:flex;align-items:center;justify-content:center"><span class="h w">Heading Here</span></div>
  <div class="abs" style="left:214px;top:42px;width:162px"><div class="h">Heading Goes Here</div><div class="tx" style="margin-top:4px">Use these image tiles to show real journeys, drivers and clients. Each tile pairs with a short heading that explains what the passenger gets from the service.</div></div>
  <div class="abs tx" style="left:12px;top:142px;width:190px">Add a short caption under the tiles to sum up the message.</div>
  <div class="foot">© Copyright 2025 KVT. All rights reserved.</div>
</section>

<!-- 17 About photo -->
<section class="slide">
  <div class="ph cabin" style="left:0;top:0;width:389px;height:219px" role="img" aria-label="Smiling man in a car"></div>
  <div class="abs" style="left:200px;top:40px;width:178px;height:120px;background:var(--teal);padding:12px 12px"><div style="font-size:10px;font-weight:600;color:#fff">About Us</div><div style="width:20px;height:1.5px;background:#fff;margin:4px 0 6px"></div><div class="tx w">We connect business travellers with professional chauffeurs in every major city. Fixed rates, live tracking and round-the-clock support keep every journey on time.</div></div>
  <div class="foot">© Copyright 2025 KVT. All rights reserved.</div>
</section>

<!-- 18 Divider -->
<section class="slide">
  <div class="ph terminal" style="inset:0" role="img" aria-label="Business people walking through an airport"></div>
  <div class="logo">KVT</div>
  <div class="abs" style="left:0;right:0;top:148px;height:42px;background:rgba(20,20,20,.9);padding:8px 30px"><div style="font-size:12px;font-weight:500;color:#fff">This Is Your Divider Page</div><div style="font-size:4.6px;color:#fff;margin-top:2px">Your Subtitle Goes Here</div></div>
</section>

<!-- 19 Quote -->
<section class="slide">
  <div class="title">Quote Area</div>
  <div class="logo">KVT</div>
  <div class="abs" style="left:0;top:50px;width:389px;height:108px;background:var(--teal)"></div>
  <div class="ph office" style="left:190px;top:40px;width:187px;height:108px" role="img" aria-label="Open notebook and laptop on a table"></div>
  <div class="abs" style="left:16px;top:66px;width:170px"><div style="font-size:6.5px;color:#fff;line-height:1.5">“ Coming together is a beginning.<br>Keeping together is progress.<br>Working together is success.</div><div style="font-size:6px;color:#fff;margin-top:8px">- Harlan Crewe -</div></div>
  <div class="foot">© Copyright 2025 KVT. All rights reserved.</div>
</section>

<!-- 20 Brand Detailed -->
<section class="slide">
  <div class="title">Brand Detailed</div>
  <div class="logo">KVT</div>
  <div class="ph terminal" style="left:12px;top:40px;width:190px;height:150px" role="img" aria-label="Family with luggage looking out of an airport window"></div>
  <div class="abs" style="left:206px;top:40px;width:84px;height:74px;background:var(--teal);padding:6px"><div class="h w">System</div><div class="tx w">Smart dispatch for every trip.</div></div>
  <div class="abs" style="left:292px;top:40px;width:84px;height:74px;background:var(--ink);padding:6px"><div class="h w">Technology</div><div class="tx w">Live tracking in our app.</div></div>
  <div class="abs" style="left:206px;top:116px;width:84px;height:74px;background:var(--teal);padding:6px"><div class="h w">Leisure</div><div class="tx w">Comfort on every journey.</div></div>
  <div class="abs" style="left:292px;top:116px;width:84px;height:74px;background:var(--grey);padding:6px"><div class="h w">Global</div><div class="tx w">Coverage in major cities.</div></div>
  <div class="foot">© Copyright 2025 KVT. All rights reserved.</div>
</section>

<!-- 21 Product Philosophy -->
<section class="slide">
  <div class="title">Product Philosophy</div>
  <div class="logo">KVT</div>
  <svg class="abs" style="left:154px;top:60px" width="80" height="80" aria-label="Donut chart"><circle cx="40" cy="40" r="30" fill="none" stroke="var(--teal)" stroke-width="14"/><circle cx="40" cy="40" r="30" fill="none" stroke="var(--grey)" stroke-width="14" stroke-dasharray="47 141" transform="rotate(-90 40 40)"/><circle cx="40" cy="40" r="30" fill="none" stroke="var(--grey-light)" stroke-width="14" stroke-dasharray="25 163" transform="rotate(-10 40 40)"/><circle cx="40" cy="40" r="14" fill="#fff" stroke="#333" stroke-width="1"/><text x="40" y="42.5" font-size="7" font-weight="700" text-anchor="middle" font-family="Montserrat,sans-serif">KVT</text></svg>
  <div class="ring" style="left:90px;top:42px;width:18px;height:18px;border-color:var(--teal)"><svg style="stroke:var(--teal)"><use href="#gear"/></svg></div>
  <div class="abs" style="left:64px;top:63px;width:70px;text-align:center"><div class="h">Secure</div><div class="tx">Safe vetted drivers.</div></div>
  <div class="ring" style="left:90px;top:120px;width:18px;height:18px;border-color:var(--teal)"><svg style="stroke:var(--teal)"><use href="#star"/></svg></div>
  <div class="abs" style="left:64px;top:141px;width:70px;text-align:center"><div class="h">Good Manager</div><div class="tx">Clear account control.</div></div>
  <div class="ring" style="left:282px;top:44px;width:18px;height:18px;border-color:var(--ink)"><svg style="stroke:var(--ink)"><use href="#user"/></svg></div>
  <div class="abs" style="left:306px;top:46px;width:70px"><div class="h">Well Organized</div><div class="tx">Every booking logged.</div></div>
  <div class="ring" style="left:282px;top:120px;width:18px;height:18px;border-color:var(--grey)"><svg style="stroke:var(--grey)"><use href="#search"/></svg></div>
  <div class="abs" style="left:306px;top:122px;width:70px"><div class="h">Illustration</div><div class="tx">Clear monthly reports.</div></div>
  <div class="foot">© Copyright 2025 KVT. All rights reserved.</div>
</section>

<!-- 22 Chart on city -->
<section class="slide">
  <div class="ph city" style="left:0;top:0;width:389px;height:160px" role="img" aria-label="Faded city skyline"></div>
  <div class="abs" style="left:150px;top:12px;font-size:4.5px;color:#333"><span style="display:inline-block;width:6px;height:4px;background:var(--teal)"></span> 2024 <span style="display:inline-block;width:6px;height:4px;background:var(--grey);margin-left:6px"></span> 2025</div>
  <svg class="abs" style="left:0;top:0" width="389" height="160" aria-label="Regional bar chart"><g font-family="Montserrat,sans-serif" font-size="5" text-anchor="middle" fill="#333">
    <rect x="40" y="78" width="16" height="82" fill="var(--grey)"/><text x="48" y="74">460</text>
    <rect x="60" y="58" width="16" height="102" fill="var(--teal)"/><text x="68" y="54">590</text>
    <rect x="130" y="70" width="16" height="90" fill="var(--grey)"/><text x="138" y="66">510</text>
    <rect x="150" y="42" width="16" height="118" fill="var(--teal)"/><text x="158" y="38">680</text>
    <rect x="220" y="100" width="16" height="60" fill="var(--grey)"/><text x="228" y="96">330</text>
    <rect x="240" y="112" width="16" height="48" fill="var(--teal)"/><text x="248" y="108">260</text>
    <rect x="310" y="112" width="16" height="48" fill="var(--grey)"/><text x="318" y="108">260</text>
    <rect x="330" y="124" width="16" height="36" fill="var(--teal)"/><text x="338" y="120">190</text></g></svg>
  <div class="abs" style="left:0;right:0;top:160px;height:50px;background:var(--ink)"></div>
  <div class="abs" style="left:28px;top:166px;width:70px"><div class="h w">Asia</div><div class="tx w">Regional growth note here.</div></div>
  <div class="abs" style="left:118px;top:166px;width:70px"><div class="h w">Africa</div><div class="tx w">Regional growth note here.</div></div>
  <div class="abs" style="left:208px;top:166px;width:70px"><div class="h w">America</div><div class="tx w">Regional growth note here.</div></div>
  <div class="abs" style="left:298px;top:166px;width:70px"><div class="h w">Euro</div><div class="tx w">Regional growth note here.</div></div>
  <div class="foot">© Copyright 2025 KVT. All rights reserved.</div>
</section>

<!-- 23 Divider dark -->
<section class="slide">
  <div class="ph night" style="inset:0;background:radial-gradient(ellipse at 30% 45%,rgba(190,200,205,.35),rgba(0,0,0,0) 55%),linear-gradient(180deg,#505356 0%,#2c2e30 60%,#141516 100%)" role="img" aria-label="Family silhouettes at an airport window"></div>
  <div class="abs" style="right:60px;top:78px;text-align:right"><div style="font-size:16px;font-weight:700;color:#fff">KVT</div></div>
  <div class="abs" style="left:150px;top:110px;right:40px;text-align:right"><div style="font-size:12px;font-weight:500;color:#fff">This Is Your Divider Page</div><div style="font-size:4.6px;color:#fff;margin-top:3px">Your Subtitle Goes Here</div></div>
</section>

<!-- 24 Trending -->
<section class="slide">
  <div class="title">Trending In The World</div>
  <div class="logo">KVT</div>
  <div class="ph map" style="left:14px;top:42px;width:270px;height:130px" role="img" aria-label="World map in light grey"></div>
  <div class="ring" style="left:26px;top:100px;width:24px;height:24px;background:var(--teal);border:none"><span style="font-size:6px;color:#fff;font-weight:600">15%</span></div>
  <div class="ring" style="left:110px;top:80px;width:40px;height:40px;background:var(--grey);border:none"><span style="font-size:9px;color:#fff;font-weight:600">80%</span></div>
  <div class="ring" style="left:230px;top:86px;width:34px;height:34px;background:var(--teal);border:none"><span style="font-size:8px;color:#fff;font-weight:600">75%</span></div>
  <div class="ring" style="left:190px;top:124px;width:18px;height:18px;background:var(--grey);border:none"><span style="font-size:5px;color:#fff">5%</span></div>
  <div class="ico sq" style="left:292px;top:50px"><svg><use href="#user"/></svg></div><div class="abs" style="left:310px;top:50px;width:68px"><div class="h t">Computer</div><div class="tx">Short trend note.</div></div>
  <div class="ico sq k" style="left:292px;top:86px"><svg><use href="#search"/></svg></div><div class="abs" style="left:310px;top:86px;width:68px"><div class="h">Infographic</div><div class="tx">Short trend note.</div></div>
  <div class="ico sq g" style="left:292px;top:122px"><svg><use href="#gear"/></svg></div><div class="abs" style="left:310px;top:122px;width:68px"><div class="h">Performance</div><div class="tx">Short trend note.</div></div>
  <div class="foot">© Copyright 2025 KVT. All rights reserved.</div>
</section>

<!-- 25 USA map -->
<section class="slide">
  <div class="title">Usa Map</div>
  <div class="logo">KVT</div>
  <div class="ph usmap" style="left:14px;top:42px;width:132px;height:84px" role="img" aria-label="Map of the United States with highlighted branch states"></div>
  <div class="abs" style="left:156px;top:44px"><div class="h" style="font-size:7px">Branches Analysis</div><div style="font-size:17px;font-weight:700;margin-top:2px">89%</div></div>
  <div class="abs tx" style="left:210px;top:60px;width:160px">Share of corporate trips covered by our own branch network.</div>
  <div class="abs tx" style="left:156px;top:84px;width:215px">Each branch runs local dispatch, vehicle checks and driver training to one shared standard.</div>
  <table class="abs" style="left:156px;top:106px;width:215px;font-size:4.4px">
    <tr style="background:var(--teal);color:#fff"><td style="padding:2px">Number</td><td>212</td><td>286</td><td>174</td><td>198</td><td style="background:var(--ink)">235</td></tr>
    <tr style="color:var(--text)"><td style="padding:2px">Total Branch</td><td>12</td><td>16</td><td>9</td><td>11</td><td>14</td></tr>
  </table>
  <div class="foot">© Copyright 2025 KVT. All rights reserved.</div>
</section>

<!-- 26 Vision & Mission -->
<section class="slide">
  <div class="title">Our Vision &amp; Mission</div>
  <div class="logo">KVT</div>
  <div class="ph teal" style="left:0;right:0;top:34px;height:170px" role="img" aria-label="Traveller with phone, teal tint"></div>
  <div class="abs" style="left:14px;top:42px;width:170px"><div style="font-size:8px;font-weight:600;color:#fff">• Our Vision:</div><div style="font-size:6.5px;font-weight:600;color:#fff;margin-top:3px">Go to the Next Level<br>Without look in the past</div><div class="tx w" style="margin-top:5px">Become the first call for every corporate travel team that needs dependable ground transport in any city.</div></div>
  <div class="abs" style="left:210px;top:42px;width:165px"><div style="font-size:8px;font-weight:600;color:#fff">• Our Missions:</div></div>
  <div class="ico" style="left:210px;top:62px;background:#fff"><svg style="stroke:var(--teal)"><use href="#tick"/></svg></div><div class="abs" style="left:228px;top:62px;width:145px"><div class="h w">Your Text Here</div><div class="tx w">Short mission note here.</div></div>
  <div class="ico" style="left:210px;top:88px;background:#fff"><svg style="stroke:var(--teal)"><use href="#tick"/></svg></div><div class="abs" style="left:228px;top:88px;width:145px"><div class="h w">Your Text Here</div><div class="tx w">Short mission note here.</div></div>
  <div class="ico" style="left:210px;top:114px;background:#fff"><svg style="stroke:var(--teal)"><use href="#tick"/></svg></div><div class="abs" style="left:228px;top:114px;width:145px"><div class="h w">Your Text Here</div><div class="tx w">Short mission note here.</div></div>
  <div class="foot">© Copyright 2025 KVT. All rights reserved.</div>
</section>

<!-- 27 Services -->
<section class="slide">
  <div class="title">Our Services</div>
  <div class="logo">KVT</div>
  <div class="ph cabin" style="left:14px;top:40px;width:150px;height:94px" role="img" aria-label="Woman driving a car"></div>
  <div class="abs" style="left:14px;top:138px;width:150px"><div class="h t">Your Title Goes Here</div><div class="tx">Introduce your service range here with a short sentence.</div></div>
  <div class="ico" style="left:180px;top:48px"><svg><use href="#tick"/></svg></div><div class="abs" style="left:200px;top:48px;width:175px"><div class="h">Service Number One</div><div class="tx">Airport transfers with meet and greet.</div></div>
  <div class="ico k" style="left:180px;top:88px"><svg><use href="#tick"/></svg></div><div class="abs" style="left:200px;top:88px;width:175px"><div class="h">Service Number Two</div><div class="tx">Hourly chauffeur hire for roadshows.</div></div>
  <div class="ico g" style="left:180px;top:128px"><svg><use href="#tick"/></svg></div><div class="abs" style="left:200px;top:128px;width:175px"><div class="h">Service Number Three</div><div class="tx">Event shuttles and group transport.</div></div>
  <div class="foot">© Copyright 2025 KVT. All rights reserved.</div>
</section>

<!-- 28 Three columns -->
<section class="slide">
  <div class="title">Three Column Description</div>
  <div class="abs" style="left:12px;top:36px;width:360px;font-size:6.5px;font-weight:500;color:var(--teal-dark)">This is place for your header text, insert your text here, just replace this text with your own text</div>
  <div class="abs" style="left:12px;top:62px;width:112px"><div class="h">Headline</div><div class="tx" style="margin-top:3px">Describe the first part of the offer here in a short paragraph of a few lines.</div><div class="tx" style="margin-top:5px">Add a supporting note with one key detail.</div></div>
  <div class="abs" style="left:138px;top:62px;width:112px"><div class="h">Headline</div><div class="tx" style="margin-top:3px">Describe the second part of the offer here in a short paragraph of a few lines.</div><div class="tx" style="margin-top:5px">Add a supporting note with one key detail.</div></div>
  <div class="abs" style="left:264px;top:62px;width:112px"><div class="h">Headline</div><div class="tx" style="margin-top:3px">Describe the third part of the offer here in a short paragraph of a few lines.</div><div class="tx" style="margin-top:5px">Add a supporting note with one key detail.</div></div>
  <div class="foot">© Copyright 2025 KVT. All rights reserved.</div>
</section>

<!-- 29 Team one -->
<section class="slide">
  <div class="title">Our Team</div>
  <div class="logo">KVT</div>
  <div class="ph face round" style="left:166px;top:30px;width:56px;height:56px;border:3px solid var(--grey-light)" role="img" aria-label="Portrait of team member"></div>
  <div class="abs" style="left:120px;top:92px;width:150px;text-align:center"><div class="h">Rowan Ashby</div><div class="tx">CEO</div></div>
  <div class="abs tx" style="left:40px;top:112px;width:150px">Leads strategy and client partnerships across all regions and fleets.</div>
  <div class="abs tx" style="left:200px;top:112px;width:150px">Former operations head with fifteen years in corporate travel.</div>
  <div class="abs" style="left:178px;top:142px;display:flex;gap:4px"><span style="width:6px;height:6px;border-radius:50%;background:var(--teal)"></span><span style="width:6px;height:6px;border-radius:50%;background:var(--teal)"></span><span style="width:6px;height:6px;border-radius:50%;background:var(--teal)"></span><span style="width:6px;height:6px;border-radius:50%;background:var(--teal)"></span></div>
  <div class="foot">© Copyright 2025 KVT. All rights reserved.</div>
</section>

<!-- 30 Subscription -->
<section class="slide">
  <div class="title">Monthly Subscription</div>
  <div class="logo">KVT</div>
  <div class="abs" style="left:0;right:0;top:90px;height:110px;background:var(--teal)"></div>
  <div class="abs" style="left:38px;top:62px;width:98px;height:120px;background:#fff;box-shadow:0 0 0 1px #ddd;text-align:center"><div style="background:var(--teal);color:#fff;font-size:9px;padding:6px 0">$300</div><div class="tx" style="line-height:2.2;margin-top:4px">Airport runs<br>Live tracking<br>Email support<br>Monthly invoice</div></div>
  <div class="abs" style="left:145px;top:54px;width:100px;height:134px;background:#fff;box-shadow:0 0 0 1px #ddd;text-align:center"><div style="background:var(--ink);color:#fff;font-size:11px;padding:8px 0">$900</div><div class="tx" style="line-height:2.2;margin-top:4px">Unlimited trips<br>Account manager<br>Priority dispatch<br>Detailed reports</div></div>
  <div class="abs" style="left:254px;top:62px;width:98px;height:120px;background:#fff;box-shadow:0 0 0 1px #ddd;text-align:center"><div style="background:var(--grey);color:#fff;font-size:9px;padding:6px 0">$400</div><div class="tx" style="line-height:2.2;margin-top:4px">City transfers<br>Live tracking<br>Phone support<br>Monthly invoice</div></div>
  <div class="foot">© Copyright 2025 KVT. All rights reserved.</div>
</section>

<!-- 31 Table -->
<section class="slide">
  <div class="title">Your Title Goes Here</div>
  <div class="logo">KVT</div>
  <table class="abs" style="left:14px;top:40px;width:360px;font-size:4.6px;color:var(--text)">
    <tr style="color:var(--ink);font-weight:600;border-bottom:1px solid var(--teal)"><td style="padding:3px">Lorem Ipsum</td><td>Date</td><td>Total</td><td>Trend</td><td>Price</td></tr>
    <tr style="background:#f3f3f3"><td style="padding:3px">Lorem Ipsum</td><td>24</td><td>18</td><td>12</td><td>15</td></tr>
    <tr><td style="padding:3px">Lorem Ipsum</td><td>31</td><td>22</td><td>16</td><td>19</td></tr>
    <tr style="background:#f3f3f3"><td style="padding:3px">Lorem Ipsum</td><td>28</td><td>20</td><td>14</td><td>17</td></tr>
    <tr><td style="padding:3px">Lorem Ipsum</td><td>36</td><td>25</td><td>18</td><td>22</td></tr>
    <tr style="background:#f3f3f3"><td style="padding:3px">Lorem Ipsum</td><td>26</td><td>19</td><td>11</td><td>13</td></tr>
    <tr><td style="padding:3px">Lorem Ipsum</td><td>33</td><td>23</td><td>17</td><td>20</td></tr>
    <tr style="background:#f3f3f3"><td style="padding:3px">Lorem Ipsum</td><td>29</td><td>21</td><td>15</td><td>18</td></tr>
    <tr><td style="padding:3px">Lorem Ipsum</td><td>38</td><td>27</td><td>19</td><td>24</td></tr>
    <tr style="background:#f3f3f3"><td style="padding:3px">Lorem Ipsum</td><td>25</td><td>17</td><td>13</td><td>16</td></tr>
    <tr><td style="padding:3px">Lorem Ipsum</td><td>30</td><td>21</td><td>14</td><td>18</td></tr>
  </table>
  <div class="foot">© Copyright 2025 KVT. All rights reserved.</div>
</section>

<!-- 32 Team four -->
<section class="slide">
  <div class="title">Our Team</div>
  <div class="logo">KVT</div>
  <div class="ph face round" style="left:16px;top:44px;width:28px;height:28px" role="img" aria-label="Portrait of team member"></div>
  <div class="abs" style="left:50px;top:42px;width:130px"><div class="h">Milo Darrow</div><div class="h t" style="font-size:4.6px">CEO</div><div class="tx">Leads growth and key accounts.</div></div>
  <div class="ph face round" style="left:200px;top:44px;width:28px;height:28px" role="img" aria-label="Portrait of team member"></div>
  <div class="abs" style="left:234px;top:42px;width:140px"><div class="h">Jonah Reade</div><div class="h t" style="font-size:4.6px">PR &amp; Art</div><div class="tx">Runs brand and client events.</div></div>
  <div class="ph face round" style="left:16px;top:104px;width:28px;height:28px" role="img" aria-label="Portrait of team member"></div>
  <div class="abs" style="left:50px;top:102px;width:130px"><div class="h">Jana Wells</div><div class="h t" style="font-size:4.6px">CEO</div><div class="tx">Oversees fleet and safety.</div></div>
  <div class="ph face round" style="left:200px;top:104px;width:28px;height:28px" role="img" aria-label="Portrait of team member"></div>
  <div class="abs" style="left:234px;top:102px;width:140px"><div class="h">Jude Corran</div><div class="h t" style="font-size:4.6px">Professor</div><div class="tx">Trains and certifies chauffeurs.</div></div>
  <div class="foot">© Copyright 2025 KVT. All rights reserved.</div>
</section>

<!-- 33 Testimonials -->
<section class="slide">
  <div class="title">Customer Testimonials</div>
  <div class="logo">KVT</div>
  <div class="ph face round" style="left:50px;top:40px;width:34px;height:34px" role="img" aria-label="Portrait of a client"></div>
  <div class="abs tx" style="left:100px;top:46px;width:200px">“The drivers are always early and the monthly report saves our travel team hours.” — Client name</div>
  <div class="abs" style="left:0;right:0;top:86px;height:90px;background:var(--ink)"></div>
  <div class="ring" style="left:46px;top:96px;width:20px;height:20px"><svg><use href="#user"/></svg></div>
  <div class="ring" style="left:136px;top:96px;width:20px;height:20px"><svg><use href="#star"/></svg></div>
  <div class="ring" style="left:226px;top:96px;width:20px;height:20px"><svg><use href="#gear"/></svg></div>
  <div class="ring" style="left:316px;top:96px;width:20px;height:20px"><svg><use href="#phone"/></svg></div>
  <div class="abs tx w" style="left:26px;top:126px;width:60px;text-align:center">Short client note.</div>
  <div class="abs tx w" style="left:116px;top:126px;width:60px;text-align:center">Short client note.</div>
  <div class="abs tx w" style="left:206px;top:126px;width:60px;text-align:center">Short client note.</div>
  <div class="abs tx w" style="left:296px;top:126px;width:60px;text-align:center">Short client note.</div>
  <div class="foot">© Copyright 2025 KVT. All rights reserved.</div>
</section>

<!-- 34 Two pictures -->
<section class="slide">
  <div class="title">Two Pictures Slide</div>
  <div class="logo">KVT</div>
  <div class="ph cabin" style="left:14px;top:42px;width:172px;height:150px" role="img" aria-label="Man smiling in a car"></div>
  <div class="ph terminal" style="left:200px;top:42px;width:176px;height:150px" role="img" aria-label="Family at an airport with luggage"></div>
  <div class="foot">© Copyright 2025 KVT. All rights reserved.</div>
</section>

<!-- 35 Title image text -->
<section class="slide">
  <div class="title">Title And Image + Text</div>
  <div class="logo">KVT</div>
  <div class="ph terminal" style="left:14px;top:40px;width:362px;height:88px" role="img" aria-label="Business travellers walking in an airport"></div>
  <div class="abs" style="left:14px;top:136px;width:150px;font-size:6.5px;font-weight:600;color:var(--teal);line-height:1.35">Reliable rides for busy teams, booked in seconds and billed once a month.</div>
  <div class="abs tx" style="left:180px;top:136px;width:95px">Every trip is tracked, every driver is vetted and every invoice is clear.</div>
  <div class="abs tx" style="left:285px;top:136px;width:92px">Fixed rates mean no surprises for your finance team at month end.</div>
  <div class="foot">© Copyright 2025 KVT. All rights reserved.</div>
</section>

<!-- 36 Sales comparison -->
<section class="slide">
  <div class="title">Sales Comparison</div>
  <div class="logo">KVT</div>
  <div class="abs h" style="left:70px;top:42px;font-size:5px">2024 Sales</div>
  <div class="abs h" style="left:276px;top:42px;font-size:5px">2025 Sales</div>
  <svg class="abs" style="left:20px;top:52px" width="150" height="90" aria-label="2024 sales bar chart"><line x1="0" y1="88" x2="150" y2="88" stroke="#ccc" stroke-width=".6"/><g fill="var(--teal)"><rect x="10" y="40" width="10" height="48"/><rect x="30" y="25" width="10" height="63"/><rect x="50" y="50" width="10" height="38"/><rect x="70" y="30" width="10" height="58"/><rect x="90" y="45" width="10" height="43"/><rect x="110" y="35" width="10" height="53"/><rect x="130" y="55" width="10" height="33"/></g></svg>
  <svg class="abs" style="left:225px;top:52px" width="150" height="90" aria-label="2025 sales bar chart"><line x1="0" y1="88" x2="150" y2="88" stroke="#ccc" stroke-width=".6"/><g fill="var(--ink)"><rect x="10" y="30" width="10" height="58"/><rect x="30" y="20" width="10" height="68"/><rect x="50" y="40" width="10" height="48"/><rect x="70" y="15" width="10" height="73"/><rect x="90" y="35" width="10" height="53"/><rect x="110" y="22" width="10" height="66"/><rect x="130" y="44" width="10" height="44"/></g></svg>
  <div class="ring" style="left:182px;top:88px;width:24px;height:24px;background:var(--grey-mid);border:none"><span style="font-size:6px;color:#fff;font-weight:600">VS</span></div>
  <div class="abs" style="left:22px;top:158px;display:flex;align-items:center;gap:5px"><span class="big" style="font-size:17px">45%</span><div class="tx" style="width:90px"><b style="color:var(--teal)">Lorem Ipsum</b><br>Share of repeat clients.</div></div>
  <div class="abs" style="left:228px;top:158px;display:flex;align-items:center;gap:5px"><span class="big" style="font-size:17px;color:var(--ink)">68%</span><div class="tx" style="width:90px"><b style="color:var(--ink)">Lorem Ipsum</b><br>Share of repeat clients.</div></div>
  <div class="foot">© Copyright 2025 KVT. All rights reserved.</div>
</section>

</main>
</body>
</html>
```